Soccer Training for Boys and Girls

I need like a flyer to post on facebook and instagram.
This is what O want to have on it.
you can use any color , soccer field on the background , or any soccer pictures.
Recreational and Travel Teams
Ages :5 to 14 years old
Field: Holloway Fenwick Middle School (4728 Meadowlark dr Silver spring, MD 20731)
Register online www.valmontekickers.example
-passing
-kicking
-shooting
-dribbling
-ball Control
Registration :$210 (includes 1st month, registration, practice Uniform
after 1st month.

Call us Phone:(240)555-0187

• kids playing soccer , soccer fields

```html
<!DOCTYPE html>
<html lang="en">
<head>
<meta charset="utf-8">
<title>Recreational &amp; Travel Teams – Valmonte Kickers Academy</title>
<link href="https://fonts.googleapis.com/css2?family=Anton&family=Montserrat:wght@500;600;700;800&display=swap" rel="stylesheet">
<style>
  :root{
    --blue:#0d4f9a;
    --yellow:#ffc20e;
    --black:#0b0b0b;
    --white:#ffffff;
    --grass-light:#6f9a45;
    --grass-dark:#1f3d1c;
  }
  *{box-sizing:border-box;margin:0;padding:0}
  html,body{width:1200px;height:1200px;overflow:hidden;background:var(--black)}
  .flyer{position:relative;width:1200px;height:1200px;background:var(--black);font-family:"Montserrat",sans-serif;overflow:hidden}
  .hero-photo{position:absolute;left:0;top:0;width:1200px;height:840px;
    background:
      radial-gradient(ellipse at 15% 0%, rgba(230,200,110,.55), transparent 45%),
      linear-gradient(180deg,var(--grass-light) 0%,#3f6b2e 38%,var(--grass-dark) 66%,var(--black) 100%);}
  .brand{position:absolute;left:790px;top:70px;width:290px;display:flex;flex-direction:column;align-items:center;gap:16px}
  .brand-mark{width:150px;height:150px;border-radius:50%;background:var(--blue)}
  .brand-name{font-family:"Montserrat",sans-serif;font-weight:800;font-size:26px;line-height:1.15;color:var(--white);text-align:center;text-transform:uppercase}
  .headline{position:absolute;left:0;top:0;width:1200px;height:1200px;pointer-events:none}
  .headline .line{font-family:"Anton",sans-serif;paint-order:stroke;stroke:var(--blue);stroke-linejoin:round}
  .headline .line-rec{fill:var(--yellow);stroke-width:14px}
  .headline .line-travel{fill:var(--white);stroke-width:16px}
  .headline .ages-band{fill:var(--white)}
  .headline .ages{font-family:"Anton",sans-serif;fill:var(--blue)}
  .field-info{position:absolute;left:102px;top:862px;padding-left:12px;border-left:3px solid var(--yellow);height:118px}
  .field-label{color:var(--yellow);font-weight:800;font-size:32px;line-height:1.1}
  .field-name{color:var(--white);font-weight:800;font-size:33px;line-height:1.25}
  .field-address{color:var(--white);font-weight:500;font-size:21px;display:flex;align-items:center;gap:8px;margin-top:4px}
  .divider{position:absolute;left:706px;top:888px;width:2px;height:94px;background:var(--white)}
  .skills{position:absolute;left:720px;top:886px;display:grid;grid-template-columns:176px auto;row-gap:4px;list-style:none}
  .skills li{display:flex;align-items:center;gap:8px;color:var(--white);font-weight:500;font-size:28px;line-height:30px}
  .skills .skill-shoot{grid-column:1}
  .yellow-band{position:absolute;left:0;top:1046px;width:1200px;height:154px;background:var(--yellow)}
  .register-box{position:absolute;left:80px;top:1007px;width:1048px;height:84px;background:var(--white);display:flex}
  .register-online{width:624px;padding:8px 12px;position:relative}
  .register-label{color:var(--blue);font-weight:700;font-size:23px}
  .register-url{color:var(--blue);font-weight:800;font-size:31px;line-height:1.1;display:flex;align-items:center;gap:4px}
  .register-url .accent{color:var(--yellow)}
  .register-rule{width:2px;background:var(--blue);margin:10px 0}
  .register-fee{padding:2px 0 0 34px}
  .fee-title{color:var(--blue);font-weight:600;font-size:30px;line-height:1.15}
  .fee-title strong{font-weight:800}
  .fee-note{color:var(--blue);font-weight:600;font-size:15.5px;line-height:1.2}
  .call{position:absolute;left:0;top:1104px;width:1200px;display:flex;align-items:center;justify-content:center;gap:14px;color:var(--blue);font-weight:800;font-size:52px}
  .call .dash{width:70px;height:4px;background:var(--blue)}
</style>
</head>
<body>
<main class="flyer">
  <div class="hero-photo" role="img" aria-label="Photo of a soccer ball on the corner line of a green turf field"></div>

  <div class="brand">
    <div class="brand-mark"></div>
    <div class="brand-name">Valmonte Kickers Academy</div>
  </div>

  <svg class="headline" viewBox="0 0 1200 1200" aria-label="Recreational and Travel Teams, ages 5 to 14 years old">
    <polygon class="ages-band" points="238,828 275,760 940,688 905,764"/>
    <g transform="translate(300 810) rotate(-7.2) skewX(-8)">
      <text class="ages" x="0" y="0" font-size="60" textLength="578" lengthAdjust="spacingAndGlyphs">Ages :5 to 14 years old</text>
    </g>
    <g transform="translate(112 624) rotate(-7) skewX(-10)">
      <text class="line line-rec" x="0" y="0" font-size="138" textLength="962" lengthAdjust="spacingAndGlyphs">RECREATIONAL</text>
    </g>
    <g transform="translate(40 752) rotate(-5.6) skewX(-10)">
      <text class="line line-travel" x="0" y="0" font-size="142" textLength="1112" lengthAdjust="spacingAndGlyphs">&amp; TRAVEL TEAMS</text>
    </g>
  </svg>

  <section class="field-info">
    <div class="field-label">Field:</div>
    <div class="field-name">Holloway Fenwick Middle School</div>
    <div class="field-address">
      <svg width="20" height="28" viewBox="0 0 20 28"><path d="M10 1a9 9 0 0 0-9 9c0 7 9 17 9 17s9-10 9-17a9 9 0 0 0-9-9z" fill="var(--yellow)"/><circle cx="10" cy="10" r="3.5" fill="var(--black)"/></svg>
      (4728 Meadowlark dr Silver spring, MD 20731)
    </div>
  </section>

  <div class="divider"></div>

  <ul class="skills">
    <li><svg width="24" height="24" viewBox="0 0 24 24"><circle cx="12" cy="12" r="11" fill="var(--yellow)"/><path d="M6.5 12.5l3.5 3.5 7-7" stroke="var(--white)" stroke-width="3" fill="none"/></svg>Passing</li>
    <li><svg width="24" height="24" viewBox="0 0 24 24"><circle cx="12" cy="12" r="11" fill="var(--yellow)"/><path d="M6.5 12.5l3.5 3.5 7-7" stroke="var(--white)" stroke-width="3" fill="none"/></svg>Dribbling</li>
    <li><svg width="24" height="24" viewBox="0 0 24 24"><circle cx="12" cy="12" r="11" fill="var(--yellow)"/><path d="M6.5 12.5l3.5 3.5 7-7" stroke="var(--white)" stroke-width="3" fill="none"/></svg>Kicking</li>
    <li><svg width="24" height="24" viewBox="0 0 24 24"><circle cx="12" cy="12" r="11" fill="var(--yellow)"/><path d="M6.5 12.5l3.5 3.5 7-7" stroke="var(--white)" stroke-width="3" fill="none"/></svg>Ball Control</li>
    <li class="skill-shoot"><svg width="24" height="24" viewBox="0 0 24 24"><circle cx="12" cy="12" r="11" fill="var(--yellow)"/><path d="M6.5 12.5l3.5 3.5 7-7" stroke="var(--white)" stroke-width="3" fill="none"/></svg>Shooting</li>
  </ul>

  <div class="yellow-band"></div>

  <section class="register-box">
    <div class="register-online">
      <div class="register-label">Register online</div>
      <div class="register-url">
        <span>www.<span class="accent">valmontekickers</span>.example</span>
        <svg width="34" height="34" viewBox="0 0 34 34"><path d="M12 10l16 10-7 1 4 8-3 1.5-4-8-5 5z" fill="var(--black)"/><path d="M8 4v4M2 10h4M3.5 5.5l3 3" stroke="var(--black)" stroke-width="2"/></svg>
      </div>
    </div>
    <div class="register-rule"></div>
    <div class="register-fee">
      <div class="fee-title">Registration: <strong>$210</strong></div>
      <div class="fee-note">(includes 1st month, registration, practice<br>Uniform after 1st month.</div>
    </div>
  </section>

  <div class="call"><span class="dash"></span>Call us Phone: (240)555-0187<span class="dash"></span></div>
</main>
</body>
</html>
```